Business card - Brio Margin - size 85 mm * 55 mm

We need new business cards. Design must fit with our vision of the firm. You find in the attached file our logo and a short description of our firm (mission, vision, value, business and so on).

Target Market(s)

Consulting firm in performance improvement

Industry/Entity Type

Management Consulting

Contact Information for Business Card

SIZE
85 mm * 55 mm
INFORMATIONS
name surname
role position
telephone number
email address

Requirements
Must have
• the brand must APPEAR for the rest Would we like to have something sleek, inspired to a "just right" approach
Should not have
• Please avoid the black color as background

```html
<!DOCTYPE html>
<html lang="en">
<head>
<meta charset="utf-8">
<title>Brio Margin – Business Card</title>
<link href="https://fonts.googleapis.com/css2?family=Arimo:wght@400;700&display=swap" rel="stylesheet">
<style>
  :root {
    --backdrop: #3b3b3b;
    --card-white: #ffffff;
    --brand-orange: #ff6600;
    --accent-green: #9cc79a;
    --text-grey: #666666;
    --rule-grey: #b5b5b5;
  }
  * { margin: 0; padding: 0; box-sizing: border-box; }
  html, body {
    width: 1105px;
    height: 1200px;
    overflow: hidden;
    background: var(--backdrop);
    font-family: "Arimo", Arial, sans-serif;
  }
  .card {
    position: absolute;
    left: 217px;
    width: 689px;
    height: 446px;
    overflow: hidden;
  }
  .card-front { top: 135px; background: var(--card-white); }
  .card-back  { top: 627px; background: var(--brand-orange); }

  /* brand lockup */
  .brand-mark {
    position: absolute;
    border-radius: 50%;
    border: 5px solid var(--brand-orange);
  }
  .brand-name {
    position: absolute;
    font-weight: 400;
    letter-spacing: 0.32em;
    white-space: nowrap;
    text-transform: uppercase;
  }
  .card-front .brand-mark { left: 442px; top: 50px; width: 116px; height: 116px; }
  .card-front .brand-name { left: 384px; top: 176px; font-size: 25px; color: var(--brand-orange); }

  .card-back .brand-mark {
    left: 266px; top: 105px; width: 152px; height: 152px;
    border-color: var(--card-white);
  }
  .card-back .brand-name {
    left: 0; right: 0; top: 282px; text-align: center;
    font-size: 34px; color: var(--card-white); padding-left: 0.32em;
  }

  /* person */
  .holder-name {
    position: absolute; left: 38px; top: 236px;
    font-size: 25px; font-weight: 700; color: var(--brand-orange);
  }
  .holder-role {
    position: absolute; left: 38px; top: 266px;
    font-size: 19px; color: var(--text-grey);
  }
  .divider {
    position: absolute; left: 38px; top: 301px;
    width: 610px; height: 1px; background: var(--rule-grey);
  }
  .contact-list {
    position: absolute; left: 38px; top: 314px;
    list-style: none;
  }
  .contact-list li {
    display: flex; align-items: center;
    height: 27.5px;
    font-size: 17px; color: var(--text-grey);
  }
  .contact-list svg { width: 17px; height: 17px; margin-right: 10px; fill: var(--brand-orange); }

  .wave { position: absolute; left: 0; bottom: 0; width: 689px; height: 60px; }
</style>
</head>
<body>

<section class="card card-front">
  <span class="brand-mark"></span>
  <span class="brand-name">Brio Margin</span>

  <h1 class="holder-name">ALAN REYES</h1>
  <p class="holder-role">President</p>
  <div class="divider"></div>

  <ul class="contact-list">
    <li>
      <svg viewBox="0 0 16 16"><path d="M3 2h3l1.5 3.5-2 1.3a8 8 0 0 0 3.7 3.7l1.3-2L14 10v3a1.5 1.5 0 0 1-1.5 1.5C7 14.5 1.5 9 1.5 3.5A1.5 1.5 0 0 1 3 2z"/></svg>
      555 0142 7781
    </li>
    <li>
      <svg viewBox="0 0 16 16"><path d="M1 3.5h14v9H1z M1 4l7 5 7-5v1.2L8 10.2 1 5.2z" fill-rule="evenodd"/><path d="M1 3.5h14L8 8.5z"/></svg>
      alan@briomargin.com
    </li>
    <li>
      <svg viewBox="0 0 16 16"><circle cx="8" cy="8" r="7"/><path d="M5 5.5c1.5-.5 2.5.5 2 1.5s-2 1-1.5 2.5 2 1 2.5 2.5M10 3.5c-.5 1.5.5 2.5 2 2.5" stroke="#fff" stroke-width="1.3" fill="none"/></svg>
      www.briomargin.com
    </li>
  </ul>

  <svg class="wave" viewBox="0 0 689 60" preserveAspectRatio="none" aria-hidden="true">
    <path d="M0 18 C180 42 430 4 689 8 L689 26 C440 22 220 36 0 40 Z" fill="var(--accent-green)"/>
    <path d="M0 40 C220 36 440 22 689 26 L689 60 L0 60 Z" fill="var(--brand-orange)"/>
  </svg>
</section>

<section class="card card-back">
  <span class="brand-mark"></span>
  <span class="brand-name">Brio Margin</span>
</section>

</body>
</html>
```